Edgey, Modern Air Conditioning Website

Quill Brothers
current website - www.pemblyhub.nz
Facebook - www.facebook.com/quillbro

We really have no idea about webdesign etc we are Engineers not Graphic artists or creative writers. We really just want a edgy, modern website completed on our behalf

We can get pictures of projects as directed or happy for you to use stock images of Varnock Lumen NZ (Heatpumps) air conditioning and exposed ducting etc

we would like the website to be heavily based on the below website. I like what they have done with both the site and the app but obviously would need to suit Quill Brothers, snowflakes heating cooling etc etc Blue and white to match our logo etc

http://gullwharfrigs.co.nz/

Need links to contact page:
Quill Brothers
37 Carrow Lane
Petone
Wellington

0800 927 514 (0800QBROLTD)

Merit.h@qbroltd.co.nz

QUILL BROTHERS
SATISFACTION GAURANTEED

WHY CHOOSE QUILL BROTHERS
EXPERIENCE COUNTS

We have a team of nationally trained and qualified Refrigeration/HVAC/Electrical Engineers and Technicians based in Petone, Wellington offering services to Wellington, Manuwatu and the Wairarapa. We are factory trained and authorised to design, service and install all major brands including Varnock, Ostrel, Pelloran Electric, Vantrigo and Brundel units. We extend our installation warranty to match that of the manufacturer’s warranty and specialise in our own diagnostics and repair.

SATISFACTION GUARANTEE
We aim to please and I put my name behind our brand! We will take care of your project from start to finish and offer a unique experience with our 100% satisfaction Guarantee*. We will supply and install your system and if your system is not installed how it was explained or not up to a trades standard we will return to make any the necessary modifications free of charge. We back this service up with our 0% upfront strategy, the power is in your hands. We will only invoice you once the installation has been completed up to a QUILL BROTHERS standard.

LOW PRESSURE SALES
Nobody likes the vacuum salesmen’s techniques and neither do we. We will come to your home or business to provide a free measure and quote. Our experience will insure this is a quick and painless experience, you will be provided with expert advice from a qualified Refrigeration Engineer, not a car salesmen turned “Heating Guru”. We will follow up with an email providing our best price straight up, installation details and online brochures. We won’t bug you with repeated phone calls and inbox clogging emails. Once we receive confirmation we will issue you with an installation date and typically have your installation completed within 10 working days.

BRANDS
www.varnocklumen.co.nz
www.ostrel.co.nz
http://plumbair.co.nz/

SERVICES
Heatpumps/Air Conditioning – Heat pumps are the most efficient way of using electricity to heat your home, but some are more efficient than others. We will select the right model for your requirements taking into account the capacity required, the visual impact of the system, the style of system, air flow and obviously your personal preferences. We only install the highest quality brands that offer outstanding after sales support. Cassettes, Consoles, Under Ceilings, Ducted, Hiwalls, Multis… Confused? Give us a call.

COMMERCIAL
We have a growing Portfolio of clients that rely on us for their Commercial requirements. We have proven ourselves to be a force to be reckoned with to be able to think outside the square and come up with unique and cost effective solutions to heat and cool large areas.

CENTRAL HEATING
Ducted Heatpumps are the holy grail of central heating and guess what? They can also cool and dehumidify your home. Ducted Heatpumps are often overlooked or priced out of reach by less experienced salesmen as its not just a point and shoot approach. We pride ourselves in our work with Ducted systems, we are able to provide quick and economic quotations and can provide expert advice on all the extra options on Ducted systems with zone control, fresh air integration, positive pressure solutions. We use the best materials when it comes to insulated ducting, mounting equipment, drainage materials. Every system we design is designed with the lowest possible decibel reading, least amount of static pressure and maximum effieciency with the help of the very latest software available.

VENTILATION
Home ventilation is a very important part of insuring you have a nice dry home to maximise the efficiency of your Heat pump. Whilst HRV systems are not designed to Heat your house they are designed to keep it dry, provide fresh filtered air to ensure your home healthy and easy to heat. We offer a number of solutions from integrated ducted heatpump systems to balanced heat recovery systems and positive air systems.

TESTIMONIALS
http://www.swapyard.co.nz/Browse/Listing.aspx?id=517362081

Target Market(s)

Home Owners

Industry/Entity Type

Air Conditioning

Colors
33a6d7
ffffff

Requirements
Must have
• Could possibly use the 'O' from Quill Brothers logo throughout website - see business Card
Nice to have
• Bright & Crisp - White and Blue
• Would love to have our Logo used throughout the website.

```html
<!DOCTYPE html>
<html lang="en">
<head>
<meta charset="utf-8">
<title>Quill Brothers – Heating &amp; Cooling</title>
<link rel="stylesheet" href="https://fonts.googleapis.com/css2?family=Questrial&display=swap">
<style>
:root{
  --blue:#29a3dc;
  --blue-dark:#1d8fc4;
  --white:#ffffff;
  --ink:#333333;
  --muted:#666666;
  --pale:#eeeeee;
  --charcoal:#2c2c2c;
  --black:#0d0d0d;
  --star:#f2b705;
}
*{box-sizing:border-box;margin:0;padding:0}
html,body{width:1200px;height:4390px;overflow:hidden}
body{font-family:"Questrial",sans-serif;color:var(--ink);background:var(--white);position:relative}
section,header,footer{position:absolute;left:0;width:1200px;overflow:hidden}
.btn{position:absolute;display:block;background:var(--blue);color:var(--white);font-size:13px;letter-spacing:1px;text-transform:uppercase;text-align:center;line-height:44px;height:44px;width:132px}

/* nav */
.nav{position:absolute;top:22px;left:0;width:1200px;height:80px}
.nav-item{position:absolute;top:0;width:100px;text-align:center;color:var(--white);font-size:12px;white-space:nowrap}
.nav-item svg{display:block;margin:0 auto 10px}
.nav-item.active::after{content:"";display:block;width:40px;height:3px;background:var(--blue);margin:8px auto 0}
.brand-name{position:absolute;left:485px;top:16px;width:230px;text-align:center;font-size:20px;letter-spacing:2px;color:var(--white);font-weight:400;white-space:nowrap}

/* hero */
.hero{top:0;height:767px;background:#1b1c1f}
.hero-photo{position:absolute;inset:0;background:linear-gradient(160deg,#3a3a3e 0%,#232427 45%,#111214 100%)}
.hero-rule{position:absolute;top:118px;left:164px;width:872px;height:2px;background:rgba(255,255,255,.35)}
.hero-title{position:absolute;top:150px;width:1200px;text-align:center;color:var(--blue);font-size:38px;font-weight:400}
.hero-lede{position:absolute;top:206px;left:270px;width:660px;text-align:center;color:var(--white);font-size:13px;line-height:24px}
.touch-title{position:absolute;top:290px;width:1200px;text-align:center;color:var(--blue);font-size:40px;font-weight:400}
.touch-sub{position:absolute;top:342px;width:1200px;text-align:center;color:var(--white);font-size:14px}
.field{position:absolute;border:1px solid rgba(255,255,255,.55);color:rgba(255,255,255,.8);font-size:12px;padding:12px 14px;height:46px;width:340px;left:248px}
.field.msg{left:614px;top:408px;width:338px;height:176px}
.hero .btn{left:522px;top:617px;width:156px}
.dots{position:absolute;top:700px;left:550px;display:flex;gap:8px}
.dots span{width:16px;height:16px;border-radius:50%;border:2px solid var(--white)}
.dots span:first-child{background:var(--white)}

/* why */
.why{top:767px;height:633px;background:var(--pale)}
.section-title{position:absolute;width:1200px;text-align:center;color:var(--blue);font-size:38px;font-weight:400}
.why .section-title{top:56px}
.feature{position:absolute;top:170px;width:260px}
.feature svg{display:block}
.feature h3{color:var(--blue);font-size:28px;line-height:30px;margin-top:36px;font-weight:400}
.feature p{margin-top:22px;font-size:12px;line-height:21px;color:var(--muted)}
.feature .btn{position:relative;margin-top:40px}

/* partners */
.partners{top:1400px;height:170px;background:var(--white)}
.partner{position:absolute;top:78px;font-size:26px;color:#222;letter-spacing:1px;white-space:nowrap}

/* services */
.services{top:1570px;height:1372px;background:var(--white)}
.services .section-title{top:16px}
.services-rule{position:absolute;top:86px;left:176px;width:848px;height:2px;background:#dddddd}
.service{position:absolute;width:415px}
.service .photo{height:235px}
.service h3{color:var(--blue);font-size:28px;line-height:30px;margin-top:40px;font-weight:400}
.service p{margin-top:26px;font-size:12px;line-height:22px;color:var(--ink)}
.service .btn{position:relative;margin-top:22px}

/* testimonials */
.testimonials{top:2942px;height:518px;background:var(--charcoal)}
.testi-bg{position:absolute;inset:0;background:linear-gradient(180deg,#3a3a3a 0%,#262626 100%)}
.testimonials .section-title{top:78px;color:var(--white);font-size:40px}
.testi-rule{position:absolute;top:140px;left:176px;width:848px;height:2px;background:rgba(255,255,255,.35)}
.quote{position:absolute;top:166px;width:416px;color:var(--white)}
.quote .mark{color:var(--blue);font-size:72px;line-height:50px;font-family:Georgia,serif}
.quote p{font-size:13px;line-height:22px;margin-top:8px}
.author{position:absolute;top:368px;display:flex;align-items:center;gap:20px;color:var(--white)}
.avatar{width:92px;height:92px;border-radius:50%;background:linear-gradient(135deg,#c9b9a8,#7c6d62)}
.author b{display:block;font-weight:400;font-size:20px}
.stars{color:var(--star);font-size:26px;letter-spacing:3px}

/* contact */
.contact{top:3460px;height:691px}
.contact-form{position:absolute;left:0;top:0;width:591px;height:691px;background:var(--blue)}
.contact-form h2{position:absolute;left:164px;top:62px;font-size:38px;color:var(--white);font-weight:400}
.c-field{position:absolute;left:164px;width:392px;height:50px;border:1px solid rgba(255,255,255,.8);color:var(--white);font-size:12px;padding:16px 14px}
.contact-form .btn{background:var(--black);left:164px;top:594px;width:158px}
.contact-visual{position:absolute;left:591px;top:0;width:609px;height:691px;background:linear-gradient(135deg,#b9b9b9 0%,#8e8e8e 60%,#6f6f6f 100%)}
.contact-details{position:absolute;left:48px;top:62px;color:var(--white);font-size:25px;line-height:40px;font-style:normal;white-space:nowrap}
.contact-details .mail{margin-top:24px;display:block;font-size:24px}
.seal{position:absolute;left:34px;top:338px}
.tagline{position:absolute;left:48px;top:470px;font-size:38px;line-height:44px;color:var(--white);text-transform:uppercase}
.tagline .lead{color:var(--blue)}

/* footer */
.footer{top:4151px;height:239px;background:var(--black)}
.footer .nav{top:70px}
.copyright{position:absolute;top:196px;width:1200px;text-align:center;color:var(--white);font-size:12px}
</style>
</head>
<body>

<header class="hero">
  <div class="hero-photo" role="img" aria-label="Dimly lit modern living room with sofa and brick wall"></div>
  <nav class="nav">
    <div class="nav-item active" style="left:208px"><svg width="22" height="22" viewBox="0 0 22 22"><path d="M2 11 11 3l9 8h-3v8h-5v-5h-2v5H5v-8z" fill="#29a3dc"/></svg>Home</div>
    <div class="nav-item" style="left:281px"><svg width="22" height="22" viewBox="0 0 22 22"><path d="M5 2h9l4 4v14H5z" fill="#29a3dc"/></svg>About Us</div>
    <div class="nav-item" style="left:378px"><svg width="22" height="22" viewBox="0 0 22 22"><circle cx="8" cy="12" r="5" fill="none" stroke="#29a3dc" stroke-width="3"/><circle cx="16" cy="6" r="3" fill="none" stroke="#29a3dc" stroke-width="2"/></svg>Services Offered</div>
    <span class="brand-name">QUILL BROTHERS</span>
    <div class="nav-item" style="left:722px"><svg width="22" height="22" viewBox="0 0 22 22"><path d="M11 21s-7-7-7-12a7 7 0 0 1 14 0c0 5-7 12-7 12z" fill="#29a3dc"/><circle cx="11" cy="9" r="2.5" fill="#1b1c1f"/></svg>Areas Serviced</div>
    <div class="nav-item" style="left:800px"><svg width="22" height="22" viewBox="0 0 22 22"><circle cx="11" cy="11" r="9" fill="#29a3dc"/><text x="11" y="15.5" text-anchor="middle" font-size="13" fill="#1b1c1f" font-family="Questrial,sans-serif">?</text></svg>FAQ's</div>
    <div class="nav-item" style="left:870px"><svg width="22" height="22" viewBox="0 0 22 22"><path d="M5 2l4 1 1 5-3 2a12 12 0 0 0 5 5l2-3 5 1 1 4c-1 2-3 3-5 3C9 20 2 13 2 7c0-2 1-4 3-5z" fill="#29a3dc"/></svg>Contact Us</div>
  </nav>
  <div class="hero-rule"></div>
  <h1 class="hero-title">Quill Brothers</h1>
  <p class="hero-lede">Lorem ipsum dolor sit amet, consectetur adipisicing elit, sed do eiusmod tempor incididunt ut labore et dolore magna aliqua. Ut enim ad minim veniam, quis nostrud exercitation ullamco.</p>
  <h2 class="touch-title">Get in Touch</h2>
  <p class="touch-sub">We will call you right back!</p>
  <div class="field" style="top:408px">Name</div>
  <div class="field" style="top:473px">Email</div>
  <div class="field" style="top:538px">Phone</div>
  <div class="field msg">Message</div>
  <a class="btn">Send Message</a>
  <div class="dots"><span></span><span></span><span></span><span></span></div>
</header>

<section class="why">
  <h2 class="section-title">Why Choose Quill Brothers</h2>
  <div class="feature" style="left:176px">
    <svg width="70" height="70" viewBox="0 0 70 70"><circle cx="35" cy="30" r="22" fill="#222"/><text x="35" y="40" text-anchor="middle" font-size="28" fill="#fff" font-family="Questrial,sans-serif">1</text><path d="M22 50l-6 16 10-4 5 7 4-16zM48 50l6 16-10-4-5 7-4-16z" fill="#222"/></svg>
    <h3>Experience<br>Counts</h3>
    <p>We have a team of nationally trained and qualified Refrigeration/HVAC/Electrical Engineers and Technicians based in Petone, Wellington offering services to Wellington, Manuwatu and the Wairarapa.</p>
    <a class="btn">Read More</a>
  </div>
  <div class="feature" style="left:466px">
    <svg width="70" height="70" viewBox="0 0 70 70"><circle cx="35" cy="26" r="18" fill="none" stroke="#222" stroke-width="5"/><path d="M25 40l-6 26 16-10 16 10-6-26z" fill="#222"/></svg>
    <h3>Satisfaction<br>Guaranteed</h3>
    <p>We aim to please and I put my name behind our brand! We will take care of your project from start to finish and offer a unique experience with our 100% satisfaction Guarantee*.</p>
    <a class="btn">Read More</a>
  </div>
  <div class="feature" style="left:756px">
    <svg width="70" height="70" viewBox="0 0 70 70"><ellipse cx="35" cy="38" rx="30" ry="18" fill="none" stroke="#222" stroke-width="4"/><path d="M10 38h50" stroke="#222" stroke-width="3"/></svg>
    <h3>Low Pressure<br>Sales</h3>
    <p>Nobody likes the vacuum salesmen's techniques and neither do we. We will come to your home or business to provide a free measure and quote.</p>
    <a class="btn">Read More</a>
  </div>
</section>

<section class="partners">
  <span class="partner" style="left:200px">Varnock Lumen NZ</span>
  <span class="partner" style="left:550px">Ostrel</span>
  <span class="partner" style="left:780px">Plumbair</span>
</section>

<section class="services">
  <h2 class="section-title">Our Services</h2>
  <div class="services-rule"></div>
  <article class="service" style="left:176px;top:128px">
    <div class="photo" role="img" aria-label="Rooftop turbine vents" style="background:linear-gradient(180deg,#d8dde2,#9aa3aa)"></div>
    <h3>Heatpumps/<br>Air Conditioning</h3>
    <p>Heat pumps are the most efficient way of using electricity to heat your home, but some are more efficient than others. We will select the right model for your requirements taking into account the capacity required, the visual impact of the system, the style of system, air flow and obviously your personal preferences.</p>
    <a class="btn">Read More</a>
  </article>
  <article class="service" style="left:609px;top:128px">
    <div class="photo" role="img" aria-label="Glass office buildings under blue sky" style="background:linear-gradient(160deg,#6fa7d8,#3f6f95 60%,#4f7a3f)"></div>
    <h3>Commercial</h3>
    <p>Heat pumps are the most efficient way of using electricity to heat your home, but some are more efficient than others. We will select the right model for your requirements taking into account the capacity required, the visual impact of the system, the style of system, air flow and obviously your personal preferences.</p>
    <a class="btn">Read More</a>
  </article>
  <article class="service" style="left:176px;top:736px">
    <div class="photo" role="img" aria-label="White radiator with thermostat valve" style="background:linear-gradient(160deg,#2d4f8c,#9fb4cf 60%,#e8edf2)"></div>
    <h3>Central<br>Heating</h3>
    <p>Heat pumps are the most efficient way of using electricity to heat your home, but some are more efficient than others. We will select the right model for your requirements taking into account the capacity required, the visual impact of the system, the style of system, air flow and obviously your personal preferences.</p>
    <a class="btn">Read More</a>
  </article>
  <article class="service" style="left:609px;top:736px">
    <div class="photo" role="img" aria-label="Outdoor condenser unit on grass" style="background:linear-gradient(180deg,#5c5f5f,#3a3d3c 60%,#6f8a4a)"></div>
    <h3>Ventilation</h3>
    <p>Heat pumps are the most efficient way of using electricity to heat your home, but some are more efficient than others. We will select the right model for your requirements taking into account the capacity required, the visual impact of the system, the style of system, air flow and obviously your personal preferences.</p>
    <a class="btn">Read More</a>
  </article>
</section>

<section class="testimonials">
  <div class="testi-bg" role="img" aria-label="Faint sketch of building interior on dark background"></div>
  <h2 class="section-title">Testimonials</h2>
  <div class="testi-rule"></div>
  <blockquote class="quote" style="left:176px"><div class="mark">“</div><p>Team Quill are amazing! Dana on admin is super friendly &amp; organised everything effortlessly. Merit &amp; Casey were very professional, gave great advice and really made the whole process easy. I was stunned with the price, and the quality of the product, workmanship and service really impressed me. I will recommend Quill to all my friends &amp; family.</p></blockquote>
  <blockquote class="quote" style="left:609px"><div class="mark">“</div><p>Merit and his team are friendly and professional and supplied and installed a high quality heat pump; the whole experience was so easy and the customised service appreciated. I contacted them to check if I could have a heat pump installed at a future date which they happily accommodated. Pricing was very competitive. Highly recommended!</p></blockquote>
  <div class="author" style="left:176px"><div class="avatar" role="img" aria-label="Customer portrait"></div><div><b>Crumb_Lad</b><span class="stars">★★★★★</span></div></div>
  <div class="author" style="left:609px"><div class="avatar" role="img" aria-label="Customer portrait"></div><div><b>Tovik</b><span class="stars">★★★★★</span></div></div>
</section>

<section class="contact">
  <div class="contact-form">
    <h2>Contact Us</h2>
    <div class="c-field" style="top:160px">Name</div>
    <div class="c-field" style="top:242px">Email</div>
    <div class="c-field" style="top:324px">Phone</div>
    <div class="c-field" style="top:406px;height:136px">Message</div>
    <a class="btn">Send Message</a>
  </div>
  <div class="contact-visual" role="img" aria-label="Smiling technician in checked shirt and overalls">
    <address class="contact-details">Quill Brothers<br>37 Carrow Lane<br>Petone &nbsp;|&nbsp; Wellington<br>0800 927 514 (0800QBROLTD)<span class="mail">Merit.h@qbroltd.co.nz</span></address>
    <svg class="seal" width="130" height="130" viewBox="0 0 130 130"><circle cx="65" cy="65" r="60" fill="#29a3dc" stroke="#fff" stroke-width="4"/></svg>
    <p class="tagline"><span class="lead">Quill Brothers</span><br>Satisfaction<br>Guaranteed</p>
  </div>
</section>

<footer class="footer">
  <nav class="nav">
    <div class="nav-item" style="left:208px"><svg width="22" height="22" viewBox="0 0 22 22"><path d="M2 11 11 3l9 8h-3v8h-5v-5h-2v5H5v-8z" fill="#29a3dc"/></svg>Home</div>
    <div class="nav-item" style="left:281px"><svg width="22" height="22" viewBox="0 0 22 22"><path d="M5 2h9l4 4v14H5z" fill="#29a3dc"/></svg>About Us</div>
    <div class="nav-item" style="left:378px"><svg width="22" height="22" viewBox="0 0 22 22"><circle cx="8" cy="12" r="5" fill="none" stroke="#29a3dc" stroke-width="3"/><circle cx="16" cy="6" r="3" fill="none" stroke="#29a3dc" stroke-width="2"/></svg>Services Offered</div>
    <span class="brand-name">QUILL BROTHERS</span>
    <div class="nav-item" style="left:722px"><svg width="22" height="22" viewBox="0 0 22 22"><path d="M11 21s-7-7-7-12a7 7 0 0 1 14 0c0 5-7 12-7 12z" fill="#29a3dc"/><circle cx="11" cy="9" r="2.5" fill="#0d0d0d"/></svg>Areas Serviced</div>
    <div class="nav-item" style="left:800px"><svg width="22" height="22" viewBox="0 0 22 22"><circle cx="11" cy="11" r="9" fill="#29a3dc"/><text x="11" y="15.5" text-anchor="middle" font-size="13" fill="#0d0d0d" font-family="Questrial,sans-serif">?</text></svg>FAQ's</div>
    <div class="nav-item" style="left:870px"><svg width="22" height="22" viewBox="0 0 22 22"><path d="M5 2l4 1 1 5-3 2a12 12 0 0 0 5 5l2-3 5 1 1 4c-1 2-3 3-5 3C9 20 2 13 2 7c0-2 1-4 3-5z" fill="#29a3dc"/></svg>Contact Us</div>
  </nav>
  <p class="copyright">© 2016 Company Name &nbsp;|&nbsp; All Rights Reserved</p>
</footer>

</body>
</html>
```